Design Awesome Business Cards for Lantern Careers

We are a Premium Resume Writing company.

1. The card is 2 sided.

2. The front side is where the logo and business information is present.

3. The other side, it will display the company's tagline
3.1. Line 1: Lifting Every Tomorrow
3.2. Line 2: by helping 1 Billion individuals in the next 10 years

4. The card must be elegant and have good design.

5. See our website to have an idea - Simplicity is key - www.Lantern-Careers.example

6. We believe in simplicity

7. The biggest part of the card is the logo - This is for the front side (Big appropriately)

8. Other information to include on front part is,
8.1. Name, Designation, mobile, email;
8.2. Company name, Business Address, Business Phone, Website

9. Colors to use: White, Red, Black

10. What not to use:
10.1. No human figures
10.2. No numbers apart of design
10.3. Nothing comical

11. Additional Notes
11.1. The card must give a wow effect
11.2. The card must be attractive
11.3. The card must be beautiful
11.4. The card must display trust and integrity
11.5. The card must be AWESOME!

12. The Design Specifications
12.1. Design must be in PSD
12.2. Resolution must be 400 or higher
12.3. Please take note, the card will be coated with matte film. Keep that in mind while designing.
12.4. All designs must be original as will be copyrighted.

Any questions, please let us know.

Thank you

```html
<!DOCTYPE html>
<html lang="en">
<head>
<meta charset="utf-8">
<title>Lantern Careers – Business Card</title>
<link href="https://fonts.googleapis.com/css2?family=Questrial&family=Montserrat:wght@400;600;700&display=swap" rel="stylesheet">
<style>
  :root {
    --page-bg: #e6e6e6;
    --brand-red: #c8102e;
    --brand-deep: #7f0a1c;
    --brand-light: #e0283f;
    --ink: #161616;
    --muted: #555555;
    --card-white: #ffffff;
  }
  * { margin: 0; padding: 0; box-sizing: border-box; }
  html, body {
    width: 1200px; height: 840px; overflow: hidden;
    background: var(--page-bg);
    font-family: "Questrial", sans-serif;
    color: var(--ink);
  }
  .sheet {
    width: 1200px; height: 840px;
    display: flex; flex-direction: column;
    align-items: center; justify-content: center; gap: 40px;
  }
  .card {
    width: 630px; height: 360px; position: relative; overflow: hidden;
    box-shadow: 0 8px 24px rgba(0,0,0,.18);
  }

  /* Front */
  .card-front { background: var(--card-white); }
  .brand {
    position: absolute; left: 36px; top: 26px;
    display: flex; align-items: center; gap: 26px;
  }
  .brand-square {
    width: 160px; height: 160px; flex: none;
    background: linear-gradient(135deg, var(--brand-light), var(--brand-deep));
  }
  .brand-name {
    font-family: "Montserrat", sans-serif; font-weight: 700;
    font-size: 54px; line-height: 1; color: var(--brand-red);
    text-transform: uppercase; letter-spacing: 1px;
  }
  .brand-tagline {
    margin-top: 12px; font-family: "Montserrat", sans-serif; font-weight: 600;
    font-size: 14px; letter-spacing: 1.8px; color: var(--ink); text-transform: uppercase;
  }
  .person { position: absolute; left: 36px; top: 196px; }
  .person-name {
    font-family: "Montserrat", sans-serif; font-weight: 600;
    font-size: 17px; line-height: 1.2; letter-spacing: 1px; color: var(--ink);
  }
  .person-role { font-size: 12px; color: var(--muted); margin-top: 1px; }
  .stripe {
    position: absolute; left: 0; right: 0; top: 244px; height: 14px;
    background: var(--brand-red); display: flex;
  }
  .stripe-accent { width: 150px; height: 100%; background: var(--ink); }
  .contact {
    position: absolute; left: 36px; right: 36px; top: 268px;
    display: flex; justify-content: space-between; font-size: 13px; line-height: 1.45;
  }
  .contact-row { display: flex; align-items: center; gap: 8px; }
  .contact-company {
    font-family: "Montserrat", sans-serif; font-weight: 700;
    color: var(--brand-red); text-transform: uppercase; font-size: 13px;
  }
  .contact-indent { padding-left: 22px; }
  .contact-web { color: var(--brand-red); }
  .icon { width: 14px; height: 14px; flex: none; }

  /* Back */
  .card-back {
    background: linear-gradient(135deg, var(--brand-light) 0%, var(--brand-red) 45%, var(--brand-deep) 100%);
    color: var(--card-white);
  }
  .back-circle {
    position: absolute; left: 200px; top: -40px; width: 320px; height: 320px;
    border-radius: 50%; background: rgba(255,255,255,.07);
  }
  .back-content { position: absolute; left: 230px; top: 110px; }
  .back-name {
    font-family: "Montserrat", sans-serif; font-weight: 700;
    font-size: 46px; line-height: 1; text-transform: uppercase; letter-spacing: 1px;
  }
  .back-tagline {
    margin-top: 26px; font-family: "Montserrat", sans-serif; font-weight: 600;
    font-size: 14px; letter-spacing: 1.5px; text-transform: uppercase;
  }
  .back-mission { margin-top: 4px; font-size: 13px; opacity: .9; }
</style>
</head>
<body>
<main class="sheet">

  <section class="card card-front" aria-label="Business card front">
    <div class="brand">
      <div class="brand-square"></div>
      <div>
        <div class="brand-name">Lantern<br>Careers</div>
        <div class="brand-tagline">Lifting Every Tomorrow</div>
      </div>
    </div>

    <div class="person">
      <div class="person-name">MARA ELLISON</div>
      <div class="person-role">Executive Director</div>
    </div>

    <div class="stripe"><div class="stripe-accent"></div></div>

    <div class="contact">
      <div class="contact-address">
        <div class="contact-row">
          <svg class="icon" viewBox="0 0 14 14"><path d="M7 1a4 4 0 0 0-4 4c0 3 4 8 4 8s4-5 4-8a4 4 0 0 0-4-4z" fill="var(--brand-red)"/><circle cx="7" cy="5" r="1.5" fill="#fff"/></svg>
          <span class="contact-company">Lantern Careers</span>
        </div>
        <div class="contact-indent">12 Harbor Lane, Port Avery</div>
        <div class="contact-indent">Westmark</div>
      </div>
      <div class="contact-lines">
        <div class="contact-row">
          <svg class="icon" viewBox="0 0 14 14"><rect width="14" height="14" rx="2" fill="var(--ink)"/><path d="M4.5 3.5l1.5 2-1 1c.6 1.2 1.3 1.9 2.5 2.5l1-1 2 1.5-1 1.5C6.5 11 3 7.5 3 4.5z" fill="#fff"/></svg>
          <span>+ 000 555 010</span>
        </div>
        <div class="contact-row">
          <svg class="icon" viewBox="0 0 14 14"><rect width="14" height="14" rx="2" fill="var(--ink)"/><rect x="4.5" y="2.5" width="5" height="9" rx="1" fill="#fff"/></svg>
          <span>+ 000 555 020</span>
        </div>
        <div class="contact-row">
          <svg class="icon" viewBox="0 0 14 14"><rect width="14" height="14" rx="2" fill="var(--ink)"/><rect x="3" y="4" width="8" height="6" fill="#fff"/><path d="M3 4l4 3 4-3" stroke="var(--ink)" fill="none"/></svg>
          <span>mara@lantern-careers.example</span>
        </div>
        <div class="contact-row">
          <svg class="icon" viewBox="0 0 14 14"><rect width="14" height="14" rx="2" fill="var(--ink)"/><circle cx="7" cy="7" r="3.5" stroke="#fff" fill="none"/><path d="M3.5 7h7M7 3.5v7" stroke="#fff"/></svg>
          <span class="contact-web">www.Lantern-Careers.example</span>
        </div>
      </div>
    </div>
  </section>

  <section class="card card-back" aria-label="Business card back">
    <div class="back-circle"></div>
    <div class="back-content">
      <div class="back-name">Lantern<br>Careers</div>
      <div class="back-tagline">Lifting Every Tomorrow</div>
      <div class="back-mission">by helping 1 billion individuals in the next 10 years</div>
    </div>
  </section>

</main>
</body>
</html>
```